Events and Parties web-site needs a Web Design

ZorVeno needs a web design.
ZorVeno means The Bees in Italian.
ZorVeno target market is people who is organizing parties and events.
Our mission is that the parties and events of our clients exceed their expectations by providing them web and mobile tools.
Our vision is to be the best and biggest party web portal of the country.
The main features of our web site is to let people invite guests and search suppliers/providers. Guests will also confirm presence (RSVP) and buy presents/gifts at the site as well.
Our slogan is "Curta sua festa desde já !" that means "Enjoy our party now !" in Brazilian Portuguese.
The idea here is that the party starts now and not only at the scheduled date and time.
Updates
It seems that must have and nice to have briefing is not appearing to you as I filled. So I will type it agai here:
Our slogan text that is "Curta sua festa desde já !" that means "Enjoy your party now !".
Space to paid ads.
Language switch to Spanish. Brazilian Portuguese is our default language.
Logon form with 2 inputs: Email and password.
RSVP form with 2 inputs: Event ID and password
Plivex trusted site seal (SSL/HTTPS) logo.
Update to my briefing: Only event organizer and guests will be able to see details of the events/parties like photos/blog, guest list and etc. Suppliers will be searched and rated like stayvorta.com/wandrikel.
Target Market(s)
ZorVeno target market is amateur and professional people who are organizing parties and events.
Our mission is that the parties and events of our clients exceed their expectations by providing them easy and fast web and mobile tools.
Our vision is to be the best and biggest party portal of our country.
The main features of our web site is to let people invite guests and search suppliers/providers. Guests will also confirm presence (RSVP) and buy presents at the site.
Industry/Entity Type
Events
Requirements
Must have
- Design and colors compliant with attached logo.
- Our slogan text that is "Curta sua festa desde já !" that means "Enjoy your party now !".
- Space to paid ads.
- Language switch to Spanish. Brazilian Portuguese is our default language.
- Logon form with 2 inputs: Email and password.
- RSVP form with 2 inputs: Event ID and password
- Plivex trusted site seal (SSL/HTTPS) logo.
Nice to have
- ZorVeno stands for The Bees in Italian. It would be very nice to have a not so explicit idea that each user is a bee and ZorVeno is the hive where party/event occurs.
Should not have
- No PageMolder please.
- No infant/child oriented designs please. Our market is not only children birthdays but also other parties and events like marriages, corporate events and so on

```html
<!DOCTYPE html>
<html lang="pt-BR">
<head>
<meta charset="utf-8">
<title>ZorVeno — Curta sua festa desde já!</title>
<link href="https://fonts.googleapis.com/css2?family=Open+Sans:ital,wght@0,300;0,400;0,600;0,700;1,300;1,400;1,700;1,800&display=swap" rel="stylesheet">
<style>
:root{
  --honey:#ffce55;
  --honey-deep:#ffc94a;
  --amber:#ffa640;
  --orange:#f28a00;
  --cocoa:#5b3a34;
  --ink:#3a1410;
  --panel:#ebe7e6;
  --card:#e7e7e7;
  --green:#3e9a60;
  --lime:#7dbb3c;
  --footer:#733e3a;
  --white:#ffffff;
  --ad-text:#a8a8a8;
}
*{margin:0;padding:0;box-sizing:border-box}
html,body{width:943px;height:1200px;overflow:hidden}
body{position:relative;background:var(--white);font-family:"Open Sans",sans-serif;color:var(--ink)}

/* header */
.site-header{position:absolute;left:0;top:0;width:943px;height:152px;background:var(--honey)}
.brand{position:absolute;left:86px;top:16px;width:108px;display:flex;flex-direction:column;align-items:center;gap:14px}
.brand-dot{width:66px;height:66px;border-radius:50%;background:var(--ink)}
.brand-name{font-size:26px;font-weight:400;color:var(--orange);line-height:34px;white-space:nowrap}
.search{position:absolute;left:206px;top:64px;width:316px;height:44px;background:var(--white);border-radius:8px}
.search-field{position:absolute;left:18px;top:12px;font-size:14px;color:var(--orange)}
.search-btn{position:absolute;right:5px;top:5px;width:86px;height:33px;border-radius:8px;background:var(--cocoa);color:var(--honey);font-weight:800;font-style:italic;font-size:14px;display:flex;align-items:center;justify-content:center}
.tagline{position:absolute;left:208px;top:121px;font-size:13.5px;font-weight:300;color:var(--ink)}
.lang{position:absolute;left:781px;top:15px;width:76px;height:18px;border-radius:4px;background:#f4c24c;display:flex;align-items:center;gap:5px;padding-left:7px;font-size:10px;color:var(--ink)}
.nav{position:absolute;left:549px;top:113px;display:flex;height:39px}
.nav a{display:flex;align-items:center;padding:0 7px;font-size:12.5px;color:var(--ink);text-decoration:none}
.nav a.active{background:#8a5a36;color:var(--honey);padding:0 8px}

/* slogan */
.slogan{position:absolute;left:0;width:943px;top:170px;text-align:center;font-size:43px;font-weight:300;font-style:italic;color:var(--ink)}

/* forms */
.form-card{position:absolute;top:249px;width:364px;height:243px;background:var(--panel);border-radius:22px;overflow:hidden}
.form-card.login{left:86px}
.form-card.rsvp{left:493px}
.form-head{height:51px;padding:14px 0 0 30px;font-size:20px;font-weight:800;font-style:italic;color:var(--ink)}
.login .form-head{background:var(--honey-deep)}
.rsvp .form-head{background:var(--amber)}
.field{position:absolute;left:25px;width:315px;height:44px;background:var(--white);border-radius:8px;padding:13px 0 0 17px;font-size:14px;color:var(--orange)}
.field.one{top:66px}
.field.two{top:124px}
.forgot{position:absolute;left:42px;top:198px;font-size:10px;color:var(--ink)}
.form-btn{position:absolute;left:214px;top:181px;width:125px;height:45px;border-radius:8px;color:var(--white);font-size:19px;font-weight:800;font-style:italic;display:flex;align-items:center;justify-content:center}
.login .form-btn{background:var(--green)}
.rsvp .form-btn{background:var(--lime)}
.or{position:absolute;left:460px;top:259px;font-size:26px;font-weight:300;font-style:italic;color:var(--ink)}

/* gallery */
.supplier{position:absolute;top:512px;width:146px;height:146px;background:var(--card)}
.supplier-photo{position:absolute;left:18px;top:12px;width:111px;height:98px}
.stars{position:absolute;left:0;width:100%;top:114px;text-align:center;color:#f5a800;font-size:17px;letter-spacing:1px}

/* content */
.content{position:absolute;left:86px;top:674px;width:622px}
.content h2{font-size:20.5px;font-weight:700;font-style:italic;color:var(--orange);line-height:28px;margin-bottom:6px}
.content p{font-size:11.9px;line-height:22.3px;margin-bottom:22.3px}
.content p.last{margin-bottom:0}
.content h2.next{margin-top:-4px}

/* ad */
.ad{position:absolute;left:720px;top:511px;width:137px;height:514px;border:1px solid #dedede;background:linear-gradient(180deg,#ececec,#f7f7f7 30%,#ececec 70%,#e6e6e6);display:flex;flex-direction:column;align-items:center;padding-top:155px;color:var(--ad-text);font-size:21px;font-weight:700;font-style:italic;line-height:35px}

/* footer */
.site-footer{position:absolute;left:0;top:1112px;width:943px;height:88px;background:var(--footer)}
.social{position:absolute;left:86px;top:39px;display:flex;gap:12px}
.social span{display:flex;align-items:center;gap:4px;font-size:11px;color:var(--honey)}
.social i{width:12px;height:12px;background:var(--honey);display:inline-block;border-radius:2px}
.foot-nav{position:absolute;right:86px;top:38px;display:flex;gap:20px}
.foot-nav a{font-size:12.5px;font-style:italic;color:var(--honey);text-decoration:none}
</style>
</head>
<body>

<header class="site-header">
  <div class="brand"><span class="brand-dot"></span><span class="brand-name">ZorVeno</span></div>
  <div class="search"><span class="search-field">Search...</span><span class="search-btn">SEARCH</span></div>
  <p class="tagline">A plataforma digital para você organizar seu evento</p>
  <div class="lang">
    <svg width="13" height="9" viewBox="0 0 13 9" aria-hidden="true"><rect width="13" height="9" fill="#2a9a3c"/><polygon points="6.5,1 12,4.5 6.5,8 1,4.5" fill="#f7d417"/><circle cx="6.5" cy="4.5" r="2" fill="#23408e"/></svg>
    Language
  </div>
  <nav class="nav">
    <a class="active" href="#">HOME</a><a href="#">ABOUT</a><a href="#">PRODUCTS</a><a href="#">SERVICES</a><a href="#">CONTACT</a>
  </nav>
</header>

<h1 class="slogan">Curta sua festa desde já!</h1>

<section class="form-card login">
  <div class="form-head">LOG IN</div>
  <div class="field one">Email...</div>
  <div class="field two">Password...</div>
  <span class="forgot">Forgotten Password</span>
  <span class="form-btn">SIGN IN</span>
</section>
<span class="or">or</span>
<section class="form-card rsvp">
  <div class="form-head">RSVP</div>
  <div class="field one">Event ID...</div>
  <div class="field two">Password...</div>
  <span class="forgot">Forgotten Password</span>
  <span class="form-btn">RSVP</span>
</section>

<div class="supplier" style="left:86px">
  <div class="supplier-photo" role="img" aria-label="Crowd dancing at a party" style="background:linear-gradient(135deg,#8a2a7a,#c43a5a 50%,#3a2a6a)"></div>
  <div class="stars">★★★★★</div>
</div>
<div class="supplier" style="left:241px">
  <div class="supplier-photo" role="img" aria-label="Bonfire night celebration" style="background:radial-gradient(circle at 60% 50%,#f0a020,#8a2a08 55%,#1a0804)"></div>
  <div class="stars">★★★★★</div>
</div>
<div class="supplier" style="left:397px">
  <div class="supplier-photo" role="img" aria-label="Decorated cupcakes on a stand" style="background:linear-gradient(160deg,#f5e08a,#e8a040 60%,#c88a50)"></div>
  <div class="stars">★★★★★</div>
</div>
<div class="supplier" style="left:552px">
  <div class="supplier-photo" role="img" aria-label="Chocolate cake with strawberries" style="background:linear-gradient(150deg,#f0e6e0,#6a3a24 50%,#b0302a)"></div>
  <div class="stars">★★★★★</div>
</div>

<article class="content">
  <h2>This where you put the content title</h2>
  <p>Lorem ipsum dolor sit amet, dico quaerendum mel cu, has ei cibo nonumy officiis, vim ancillae mentitum id. His ea scaevola platonem delicata, atqui minim verear duo in. Possim ponderum perpetua ea vim, est veri suscipit consequat no, saepe docendi consulatu per cu. Sed fugit sonet insolens cu, pro ex veri saepe.</p>
  <p>Nec at vero sonet quaeque, ius vivendum legendos no. Vix id semper essent, nec ut movet scaevola. Cu cibo natum dissentiunt usu, ex ius suscipit platonem splendide. Doctus sanctus forensibus sed<br>an, elit recusabo sed in. Timeam principes iracundia ea ius, te mel habeo fugit vitae.</p>
  <h2 class="next">Another heading</h2>
  <p>Vidisse tibique est in, hinc integre fastidii ex eum, ornatus utroque vis ei. Vim novum fierent id, cu omittam qualisque eam. Et vix summo primis audiam, cum ea iriure impedit scribentur. Cum no idque tibique, erroribus salutatus scribentur ex vix. Eius nullam dolorem id qui, mea ne tollit altera ancillae.</p>
  <p class="last">Cu minimum consectetuer eam, at habeo causae verterem duo, id meliore evertitur disputationi sed. Est ei sale conceptam, vel id aliquam sanctus vituperatoribus. Adhuc fabulas moderatius nam an. Eos ut omnesque consetetur ullamcorper. Vis ex assueverit philosophia, ut quot autem recteque his, id consulatu consequuntur qui.</p>
</article>

<aside class="ad"><span>160x600</span><span>Banner Ad</span></aside>

<footer class="site-footer">
  <div class="social"><span><i></i>Friendora</span><span><i></i>Chirply</span><span><i></i>Pictagon</span></div>
  <nav class="foot-nav"><a href="#">Home</a><a href="#">About</a><a href="#">Products</a><a href="#">Services</a><a href="#">Contact</a></nav>
</footer>

</body>
</html>
```